Poster to promote Global Critter Care Fest

Hi Designers,

Animal lovers all over the world are grateful for the work of vets.

To recognize all their efforts, Global Critter Care Fest takes place globally on April 30. This year's theme is 'Continuing education with a one health focus'.

It's about working alongside the human health sector to tackle animal disease and food safety. Read more here: http://www.kalvora.int/for-the-media/press-releases/detail/article/global-critter-care-fest-award-2016/

We want you to design a poster to promote the day, and the key message.

The poster must feature:
- the words 'Global Critter Care Fest'
- the date 'April 30, 2016'
- the theme 'Continuing education with a one health focus

You can choose any imagery and colors you feel will be engaging for the audience and will reflect the industry and messages.

Think animal, vets, pets, caring, health.

Looking forward to seeing your ideas.

Thanks

Pixelhive

Veterinary

• - the words 'Global Critter Care Fest'
• - the date 'April 30, 2016'
• - the theme 'Continuing education with a one health focus

```html
<!DOCTYPE html>
<html lang="en">
<head>
<meta charset="utf-8">
<title>Global Critter Care Fest – April 30, 2016</title>
<link rel="stylesheet" href="https://fonts.googleapis.com/css2?family=Open+Sans:wght@400;600&display=swap">
<style>
  :root {
    --ink: #55506a;
    --date-red: #b8201e;
    --partner-olive: #8c9a3c;
    --partner-red: #a51c30;
    --badge-grey: #9a9aa4;
    --paper: #ffffff;
  }
  * { margin: 0; padding: 0; box-sizing: border-box; }
  html, body { width: 855px; height: 1200px; overflow: hidden; background: var(--paper); }
  .poster {
    position: relative;
    width: 855px;
    height: 1200px;
    background: var(--paper);
    font-family: "Open Sans", Arial, sans-serif;
    color: var(--ink);
  }
  .event-title {
    position: absolute;
    left: 84px;
    top: 68px;
    font-weight: 600;
    font-size: 98px;
    line-height: 104px;
    letter-spacing: -0.5px;
  }
  .event-title span { display: block; }
  .event-date {
    position: absolute;
    left: 86px;
    top: 400px;
    font-size: 38px;
    font-weight: 400;
    color: var(--date-red);
  }
  .animal-strip {
    position: absolute;
    left: 0;
    top: 494px;
    width: 855px;
    height: 274px;
    display: flex;
    gap: 2px;
  }
  .animal-panel { height: 100%; flex: 1 1 0; }
  .panel-pigeon { flex-basis: 173px; background: radial-gradient(circle at 50% 70%, #4a3a7a 0%, #3d4f72 35%, #a9c86a 75%, #cfe29a 100%); }
  .panel-pony { background: linear-gradient(180deg, #6aa6dc 0%, #c9dcec 30%, #8b6446 60%, #5a4030 100%); }
  .panel-cow { background: linear-gradient(180deg, #dfe4e8 0%, #3a3130 35%, #2a2524 60%, #6c9a3a 100%); }
  .panel-ostrich { background: linear-gradient(180deg, #8ec0e6 0%, #c5dced 35%, #7ea860 55%, #a89a90 75%, #c4b4a8 100%); }
  .panel-terrier { flex-basis: 173px; background: radial-gradient(circle at 55% 60%, #b07a3a 0%, #8d5a2a 45%, #97a948 90%); }
  .theme {
    position: absolute;
    left: 86px;
    top: 808px;
    font-weight: 600;
    font-size: 40px;
    line-height: 48px;
  }
  .theme-label {
    position: absolute;
    left: 85px;
    top: 928px;
    font-size: 16px;
    letter-spacing: 0.4px;
    text-transform: uppercase;
  }
  .partner {
    position: absolute;
    display: flex;
    align-items: center;
    gap: 8px;
    font-weight: 600;
    font-size: 28px;
  }
  .partner-vetlink { left: 86px; top: 1088px; color: var(--partner-olive); }
  .partner-kalvora { left: 640px; top: 1088px; color: var(--partner-red); }
  .partner-dot { width: 14px; height: 14px; border-radius: 50%; background: currentColor; }
  .event-badge { position: absolute; left: 366px; top: 1046px; }
</style>
</head>
<body>
  <main class="poster">
    <h1 class="event-title"><span>Global</span><span>Critter Care</span><span>Fest</span></h1>
    <p class="event-date">April 30, 2016</p>

    <section class="animal-strip">
      <div class="animal-panel panel-pigeon" role="img" aria-label="Close-up photo of a pigeon with iridescent purple plumage"></div>
      <div class="animal-panel panel-pony" role="img" aria-label="Photo of a shaggy brown pony under a blue sky"></div>
      <div class="animal-panel panel-cow" role="img" aria-label="Photo of a black and white horned cow in a field"></div>
      <div class="animal-panel panel-ostrich" role="img" aria-label="Photo of an ostrich looking into the camera"></div>
      <div class="animal-panel panel-terrier" role="img" aria-label="Close-up photo of a happy Yorkshire terrier"></div>
    </section>

    <h2 class="theme">Continuing education<br>with a one health focus</h2>
    <p class="theme-label">Selected theme 2016</p>

    <div class="partner partner-vetlink"><span class="partner-dot"></span>Vetlink</div>

    <svg class="event-badge" width="124" height="124" viewBox="0 0 124 124" role="img" aria-label="Event badge">
      <circle cx="62" cy="62" r="60" fill="none" stroke="var(--badge-grey)" stroke-width="2"/>
      <circle cx="62" cy="62" r="44" fill="#e4e4ea"/>
    </svg>

    <div class="partner partner-kalvora">Kalvora<span class="partner-dot"></span></div>
  </main>
</body>
</html>
```